ラベルデザインコンセプト  現在ミルダンで展開しているシリーズをあまり意識せずに独自の考えにもとずいてデザインして欲しい。自然感、植物感を大切に、写真ではなく、やさしいイラストがいいと考えている。
高品質なお茶を身近に感じる素朴さを。
1つ1つ特別なこだわりをもって作られたお茶を感じつつ、「健康茶」という一般的に感じるイメージよりも「おいしく飲めるお茶、自然感」を大事に高級と素朴さを兼ね備えた生活の中に馴染むヴィジュアルデザイン。

桐野農園または、各商品のブランディングデザインも兼ねたプロダクトデザインとなりえるデザインの統一を考えられたデザイン。
(ブランドロゴやマークなどの統一化を考えられたもの) ロゴマークは現在ミルダンで使用しているロゴマークを使用してください。

国産穀物茶
「原材料」 とうもろこし、あずき、はと麦、有機玄米、ごぼう 原料はすべて国産品を使用している。「こだわり」国産の産品を、こだわり製法で仕上げ、健康茶として美味しく仕上げた。穀物類にごぼうを加えて美味しく仕上げている。
国産よもぎ茶
「原材料」国産よもぎ、収穫したよもぎを乾燥したものをお茶にしてます。よもぎの香り味を大切に、お茶として楽しめるように。よもぎのやさしい香りを頂ける。
国産びわ茶
「原材料」国産びわ茶 国産のびわの葉を収穫乾燥している。びわの葉の美味しさを楽しむため、敢えて焙煎はしていない。びわの葉は分検討ではビタミンEの一種であるトコフェロールを含んでおり、抗酸化に力を発揮すると言われている。

ラベルのサイズは11.5センチ×11.5センチ、和紙でも合いそうなシールデザイン。パッケージとなる袋はアルミクラフトを考えている。

詳しくは添付資料を見てください。

今回ご提案ありがとうございます。沢山の提案の中から選ばせて頂きました。1,視認性が良いこと。2,独自性がある事。3,パッケージが女性に向けやさしいこと。が、大きな要因でした。女性数十名にアンケートを取り選定しておりましたので時間がかかりましたが、いいものを選択できたと思っています。

今回沢山のデザインを提案いただき誠にありがとうございました。最終女性数十名にアンケートを出して選定をしており返事が遅れ申し訳ありませんでした。最終的に視認性がよく、シンプルで、かわいらしいパッケージが選択されました。イラストやデザインについては、優れたものを沢山提案頂きありがとうございました。また、機会がありましたらよろしくお願いします。

```html
<!DOCTYPE html>
<html lang="ja">
<head>
<meta charset="utf-8">
<title>桐野農園 国産茶ラベル</title>
<link rel="stylesheet" href="https://fonts.googleapis.com/css2?family=M+PLUS+Rounded+1c:wght@500;700;800&family=Noto+Sans+JP:wght@400;500;700&display=swap">
<style>
  :root {
    --bg: #ffffff;
    --paper: #f8f6f0;
    --paper-edge: #ece8dd;
    --title: #6b4a2c;
    --ink: #5a4a3a;
    --spec: #777777;
    --badge-brown: #8a6a3e;
    --badge-olive: #a6a23c;
    --badge-green: #7da23e;
    --badge-orange: #dca53c;
    --leaf-green: #8fb35a;
    --leaf-dark: #5f8a3a;
    --grain-gold: #d8b25a;
    --loquat: #eeb544;
  }
  * { margin: 0; padding: 0; box-sizing: border-box; }
  html, body { width: 1200px; height: 2280px; overflow: hidden; background: var(--bg); }
  body { position: relative; font-family: "Noto Sans JP", sans-serif; color: var(--ink); }

  .spec { position: absolute; left: 44px; top: 36px; font-size: 20px; line-height: 1.55; color: var(--spec); }

  .label {
    position: absolute; left: 250px; width: 700px; height: 700px;
    border-radius: 50%; overflow: hidden;
    background: radial-gradient(circle at 50% 45%, var(--paper) 60%, var(--paper-edge) 100%);
    box-shadow: 0 2px 10px rgba(0,0,0,0.08);
  }
  .label--grain { top: 50px; }
  .label--yomogi { top: 778px; }
  .label--biwa { top: 1510px; }

  .art { position: absolute; }
  .art--left { left: 0; top: 0; width: 190px; height: 700px; }
  .art--right { right: 0; top: 0; width: 190px; height: 700px; }
  .art--top { left: 170px; top: 0; width: 360px; height: 110px; }

  .label--grain .art--left { background: linear-gradient(90deg, rgba(150,140,110,0.55), rgba(150,140,110,0)); }
  .label--grain .art--right { background: linear-gradient(270deg, rgba(216,178,90,0.7), rgba(143,179,90,0.25) 60%, rgba(143,179,90,0)); }
  .label--grain .art--top { background: radial-gradient(ellipse at 50% 0%, rgba(200,180,120,0.45), rgba(200,180,120,0) 70%); }

  .label--yomogi .art--left { background: linear-gradient(90deg, rgba(95,138,58,0.6), rgba(143,179,90,0)); }
  .label--yomogi .art--right { background: linear-gradient(270deg, rgba(95,138,58,0.6), rgba(143,179,90,0)); }
  .label--yomogi .art--top { background: radial-gradient(ellipse at 50% 0%, rgba(143,179,90,0.55), rgba(143,179,90,0) 70%); }

  .label--biwa .art--left { background: linear-gradient(90deg, rgba(238,181,68,0.65), rgba(143,179,90,0.25) 60%, rgba(143,179,90,0)); }
  .label--biwa .art--right { background: linear-gradient(270deg, rgba(238,181,68,0.65), rgba(143,179,90,0.25) 60%, rgba(143,179,90,0)); }
  .label--biwa .art--top { background: radial-gradient(ellipse at 50% 0%, rgba(143,179,90,0.45), rgba(143,179,90,0) 70%); }

  .title { position: absolute; left: 0; width: 700px; text-align: center; font-family: "M PLUS Rounded 1c", sans-serif; font-weight: 800; color: var(--title); }
  .title__origin { top: 132px; font-size: 92px; line-height: 1; letter-spacing: 4px; }
  .title__name { top: 238px; font-size: 116px; line-height: 1; letter-spacing: 2px; }

  .tagline { position: absolute; left: 0; top: 402px; width: 700px; text-align: center; font-size: 20px; font-weight: 500; line-height: 1.5; color: var(--ink); }

  .badges { position: absolute; left: 0; top: 484px; width: 700px; display: flex; justify-content: center; gap: 18px; }
  .badge {
    width: 108px; height: 108px; border-radius: 50%;
    display: flex; align-items: center; justify-content: center; text-align: center;
    color: #fff; font-size: 17px; font-weight: 700; line-height: 1.3;
  }
  .badge--brown { background: var(--badge-brown); }
  .badge--olive { background: var(--badge-olive); }
  .badge--green { background: var(--badge-green); }
  .badge--orange { background: var(--badge-orange); }

  .brand { position: absolute; left: 0; top: 616px; width: 700px; text-align: center; color: var(--title); }
  .brand__lead { font-size: 11px; letter-spacing: 1px; }
  .brand__name { display: inline-flex; align-items: center; gap: 8px; font-size: 30px; font-weight: 700; font-family: "Noto Sans JP", sans-serif; }
  .brand__mark { width: 22px; height: 22px; background: var(--title); }
</style>
</head>
<body>
  <p class="spec">サイズ：115Φ (mm)<br>色　数：フルカラー(CMYK)</p>

  <section class="label label--grain">
    <div class="art art--left" role="img" aria-label="あずきとはと麦の穂の水彩イラスト"></div>
    <div class="art art--right" role="img" aria-label="とうもろこしと穀物の葉の水彩イラスト"></div>
    <div class="art art--top" role="img" aria-label="玄米とごぼうの水彩イラスト"></div>
    <h1 class="title title__origin">国産</h1>
    <h2 class="title title__name">穀物茶</h2>
    <p class="tagline">豊富な食物繊維でおいしく腸活<br>ホットですっきりおいしい</p>
    <div class="badges">
      <span class="badge badge--brown">豊富な<br>食物繊維</span>
      <span class="badge badge--olive">ノン<br>カフェイン</span>
      <span class="badge badge--green">無漂白<br>ティーバッグ</span>
    </div>
    <div class="brand">
      <div class="brand__lead">自然と暮らす やさしいお茶</div>
      <div class="brand__name"><span class="brand__mark"></span>桐野農園</div>
    </div>
  </section>

  <section class="label label--yomogi">
    <div class="art art--left" role="img" aria-label="よもぎの葉の水彩イラスト"></div>
    <div class="art art--right" role="img" aria-label="よもぎの葉の水彩イラスト"></div>
    <div class="art art--top" role="img" aria-label="よもぎの若葉の水彩イラスト"></div>
    <h1 class="title title__origin">国産</h1>
    <h2 class="title title__name">よもぎ茶</h2>
    <p class="tagline">アロマのようなやさしいよもぎの香りでリラックス<br>ホットでもアイスでもおいしい</p>
    <div class="badges">
      <span class="badge badge--green">ホットでも<br>アイスでも</span>
      <span class="badge badge--olive">ノン<br>カフェイン</span>
      <span class="badge badge--green">無漂白<br>ティーバッグ</span>
    </div>
    <div class="brand">
      <div class="brand__lead">自然と暮らす やさしいお茶</div>
      <div class="brand__name"><span class="brand__mark"></span>桐野農園</div>
    </div>
  </section>

  <section class="label label--biwa">
    <div class="art art--left" role="img" aria-label="びわの実と葉の水彩イラスト"></div>
    <div class="art art--right" role="img" aria-label="びわの実と葉の水彩イラスト"></div>
    <div class="art art--top" role="img" aria-label="びわの葉の水彩イラスト"></div>
    <h1 class="title title__origin">国産</h1>
    <h2 class="title title__name">びわ茶</h2>
    <p class="tagline">抗酸化作用のあるトコフェロールを含有<br>国産びわの葉のおいしさをしっかり味わえるお茶</p>
    <div class="badges">
      <span class="badge badge--orange">トコフェ<br>ロール含有</span>
      <span class="badge badge--olive">ノン<br>カフェイン</span>
      <span class="badge badge--green">無漂白<br>ティーバッグ</span>
    </div>
    <div class="brand">
      <div class="brand__lead">自然と暮らす やさしいお茶</div>
      <div class="brand__name"><span class="brand__mark"></span>桐野農園</div>
    </div>
  </section>
</body>
</html>
```